Business Card Design Project - bel soravin group

dear Sirs

we need business card design for our group ( BEL Soravin Group ) , i have got the Logo design of our group from pixel harbor in previous , so all need details relating to our group i think available with you, as well as the the chosen logo design

we hope to provide us with business card logo that to be appropaite and satisfactory to us .

thanks

note : logo design of our group is attached .
Updates

Reason: please extend the deadline of my project for additional 15 days because i didn't received appropriate design for our gruop yet . kindly beaware that i have received 77 design till now , supossed to send me 200-250 design at least . thanks

Target Market(s)

contents
-

name : Korvan EL Mistrani

position : Operation Manager

Industry/Entity Type

Business

Requirements
Must have

• person name

group logo
Nice to have
• logo color matching with back background

```html
<!DOCTYPE html>
<html lang="en">
<head>
<meta charset="utf-8">
<title>BEL Soravin Group – Foldable Business Card</title>
<link rel="stylesheet" href="https://fonts.googleapis.com/css2?family=Archivo+Narrow:wght@500;600;700&family=Caveat:wght@600&display=swap">
<style>
  :root {
    --paper: #ffffff;
    --card-blue: #7889a0;
    --card-yellow: #e3c56a;
    --card-edge: #56687d;
    --brand-blue: #1d4f9c;
    --ink: #111111;
    --contact-ink: #6c7f97;
  }
  html, body {
    margin: 0;
    padding: 0;
    width: 1200px;
    height: 1043px;
    overflow: hidden;
    background: var(--paper);
  }
  .sheet { display: block; width: 1200px; height: 1043px; }
  .spec-note {
    font-family: "Archivo Narrow", "Arial Narrow", sans-serif;
    font-weight: 600;
    font-size: 15px;
    fill: var(--ink);
  }
  .panel-blue { fill: var(--card-blue); }
  .panel-yellow { fill: var(--card-yellow); }
  .card-outline { fill: none; stroke: var(--card-edge); stroke-width: 1.2; }
  .brand-name {
    font-family: "Archivo Narrow", "Arial Narrow", sans-serif;
    font-weight: 700;
    font-size: 44px;
    fill: var(--brand-blue);
  }
  .brand-sub {
    font-family: "Archivo Narrow", "Arial Narrow", sans-serif;
    font-weight: 700;
    font-size: 26px;
    letter-spacing: 6px;
    fill: var(--brand-blue);
  }
  .web-address {
    font-family: "Archivo Narrow", "Arial Narrow", sans-serif;
    font-weight: 500;
    font-size: 20px;
    fill: var(--card-yellow);
  }
  .tagline {
    font-family: "Caveat", cursive;
    font-weight: 600;
    font-size: 30px;
    fill: var(--card-yellow);
  }
  .contact-name {
    font-family: "Archivo Narrow", "Arial Narrow", sans-serif;
    font-weight: 600;
    font-size: 22px;
    fill: var(--contact-ink);
  }
  .contact-line {
    font-family: "Archivo Narrow", "Arial Narrow", sans-serif;
    font-weight: 500;
    font-size: 21px;
    letter-spacing: 0.5px;
    fill: var(--contact-ink);
  }
</style>
</head>
<body>
<svg class="sheet" viewBox="0 0 1050 913" xmlns="http://www.w3.org/2000/svg" role="img" aria-label="Foldable business card layout for BEL Soravin Group, front and back">

  <!-- Specification notes -->
  <g class="spec-notes">
    <text class="spec-note" transform="translate(979,50) rotate(90)">It is a foldable card with blue as a front  as front</text>
    <text class="spec-note" transform="translate(956,50) rotate(90)">and yellow part follows it.</text>
    <text class="spec-note" transform="translate(899,50) rotate(90)">Card Dimensions</text>
    <text class="spec-note" transform="translate(877,50) rotate(90)">(Rectangular part) 72mm * 52mm</text>
    <text class="spec-note" transform="translate(854,50) rotate(90)">(Curved Part) 52mm * 57.6mm</text>
    <text class="spec-note" transform="translate(809,50) rotate(90)">Font used</text>
    <text class="spec-note" transform="translate(764,50) rotate(90)">Franklin Gothic Medium</text>
    <text class="spec-note" transform="translate(742,50) rotate(90)">size 11 and 10pt</text>
    <text class="spec-note" transform="translate(694,50) rotate(90)">Arab Dances</text>
    <text class="spec-note" transform="translate(672,50) rotate(90)">size 12</text>
  </g>

  <!-- Card front (outer face) -->
  <g class="card-front">
    <rect class="panel-yellow" x="22" y="35" width="574" height="398"/>
    <path class="panel-blue" d="M235,35 Q78,234 240,433 L596,433 L596,35 Z"/>
    <rect class="card-outline" x="22" y="35" width="574" height="398"/>
    <text class="brand-name" transform="translate(398,250) rotate(90)" text-anchor="middle">BEL SORAVIN</text>
    <text class="brand-sub" transform="translate(362,250) rotate(90)" text-anchor="middle">GROUP</text>
  </g>

  <!-- Card inside (contact face with curved flap) -->
  <g class="card-inside">
    <rect class="panel-yellow" x="22" y="482" width="574" height="398"/>
    <path class="panel-blue" d="M596,482 L935,482 Q1030,482 1030,625 L1030,737 Q1030,880 935,880 L596,880 Z"/>
    <path class="card-outline" d="M22,482 L935,482 Q1030,482 1030,625 L1030,737 Q1030,880 935,880 L22,880 Z"/>

    <text class="web-address" transform="translate(616,555) rotate(90)">www.belsoravingroup.com</text>

    <g class="tagline-block">
      <text class="tagline" transform="translate(876,598) rotate(90)">We Promise</text>
      <text class="tagline" transform="translate(838,598) rotate(90)">High Quality</text>
      <text class="tagline" transform="translate(800,598) rotate(90)">Honesty and</text>
      <text class="tagline" transform="translate(762,598) rotate(90)">Integrity</text>
    </g>

    <g class="contact-block">
      <text class="contact-name" transform="translate(484,690) rotate(90)" text-anchor="middle">Korvan EL Mistrani</text>
      <text class="contact-line" transform="translate(449,690) rotate(90)" text-anchor="middle">(Operational Manager)</text>
      <text class="contact-line" transform="translate(399,682) rotate(90)" text-anchor="middle">Mob: 5521*********</text>
      <text class="contact-line" transform="translate(364,690) rotate(90)" text-anchor="middle">Tel: 022-464646*</text>
      <text class="contact-line" transform="translate(329,690) rotate(90)" text-anchor="middle">Fax: 535313**</text>
    </g>
  </g>
</svg>
</body>
</html>
```